Business card design needed

i need a business card designed for my hair salon its call parlour 71 i want the cards to look similar to the velvet 88 design a big 71 with studio written in the top part of the 3.The 71 big on the left side then all my details (number address name) would love it to be a vintage look, colours to be in black and white/silver card to b black.
to have a line on the back with appointment day time, also would love a vip card like the vip drink card but with free treatments or shampoo so five visits that can b stamped and get a free treatment then 10th get 10% off... or something like that...
Industry/Entity Type
Hair
Contact Information for Business Card
Parlour 71
Mira Dunwoody
0431279406
71 Orchard Crescent, Tallow Bend

```html
<!DOCTYPE html>
<html lang="en">
<head>
<meta charset="utf-8">
<title>Parlour 71 – Business Cards</title>
<link rel="stylesheet" href="https://fonts.googleapis.com/css2?family=Marcellus&family=Arimo:wght@400&display=swap">
<style>
  :root {
    --page-bg: #e9e7e4;
    --card-black: #050505;
    --silver-light: #f2f2f2;
    --silver-mid: #b9b9b9;
    --silver-dark: #7d7d7d;
    --ink-dark: #1a1a1a;
    --panel-grey: #cfcfcf;
    --panel-line: #8a8a8a;
  }
  * { margin: 0; padding: 0; box-sizing: border-box; }
  html, body { width: 1200px; height: 900px; overflow: hidden; }
  body { background: var(--page-bg); position: relative; font-family: "Arimo", sans-serif; }

  .card {
    position: absolute;
    width: 560px;
    height: 320px;
    background: var(--card-black);
    border-radius: 26px;
    overflow: hidden;
    box-shadow: 0 10px 30px rgba(0,0,0,0.25);
  }
  .card--back { left: 80px; top: 80px; }
  .card--front { left: 560px; top: 500px; }

  /* Back: appointment card */
  .brand-plate {
    position: absolute;
    left: 148px; top: 0;
    width: 262px; height: 184px;
    background: linear-gradient(115deg, var(--silver-dark) 0%, var(--silver-light) 35%, var(--silver-mid) 55%, var(--silver-light) 75%, var(--silver-dark) 100%);
    display: flex; align-items: center; justify-content: center;
  }
  .brand-name {
    font-family: "Marcellus", serif;
    font-size: 40px;
    letter-spacing: 2px;
    color: var(--ink-dark);
  }
  .appointment-slip {
    position: absolute;
    left: 236px; top: 206px;
    width: 250px;
    height: 88px;
  }
  .appointment-slip svg { position: absolute; inset: 0; }
  .appointment-title {
    position: absolute; left: 20px; top: 14px;
    font-size: 13px; color: var(--ink-dark);
  }
  .appointment-field {
    position: absolute; left: 20px;
    font-size: 8px; color: var(--ink-dark); text-transform: uppercase;
  }
  .appointment-field--date { top: 46px; }
  .appointment-field--time { top: 66px; }

  /* Front: contact card */
  .card-frame { position: absolute; inset: 0; }
  .front-brand {
    position: absolute; left: 26px; top: 38px;
    font-family: "Marcellus", serif;
    font-size: 44px;
    letter-spacing: 2px;
    color: var(--silver-mid);
  }
  .contact-name {
    position: absolute; left: 290px; top: 70px;
    font-family: "Marcellus", serif;
    font-size: 22px; letter-spacing: 1px;
    color: var(--silver-mid);
  }
  .contact-phone {
    position: absolute; left: 250px; top: 186px;
    font-size: 17px; letter-spacing: 1px;
    color: var(--silver-mid);
  }
  .contact-address {
    position: absolute; left: 180px; top: 248px;
    font-size: 16px; letter-spacing: 0.5px;
    color: var(--silver-mid);
  }
</style>
</head>
<body>

  <section class="card card--back" aria-label="Appointment card">
    <div class="brand-plate">
      <span class="brand-name">Parlour 71</span>
    </div>
    <div class="appointment-slip">
      <svg width="250" height="88" viewBox="0 0 250 88" aria-hidden="true">
        <path d="M14 6 H236 Q244 6 244 14 V20 H250 V72 H244 V80 Q244 88 236 88 H14 Q6 88 6 80 V74 H0 V22 H6 V14 Q6 6 14 6 Z"
              fill="var(--panel-grey)" stroke="#ffffff" stroke-width="1.5"/>
        <line x1="150" y1="24" x2="232" y2="24" stroke="var(--panel-line)" stroke-width="1"/>
        <line x1="46" y1="56" x2="232" y2="56" stroke="var(--panel-line)" stroke-width="1"/>
        <line x1="46" y1="76" x2="232" y2="76" stroke="var(--panel-line)" stroke-width="1"/>
      </svg>
      <span class="appointment-title">Your next appointment:</span>
      <span class="appointment-field appointment-field--date">Date:</span>
      <span class="appointment-field appointment-field--time">Time:</span>
    </div>
  </section>

  <section class="card card--front" aria-label="Contact card">
    <svg class="card-frame" width="560" height="320" viewBox="0 0 560 320" aria-hidden="true">
      <path d="M250 16 H528 Q544 16 544 32 V288 Q544 304 528 304 H32 Q16 304 16 288 V150"
            fill="none" stroke="var(--silver-mid)" stroke-width="3"/>
    </svg>
    <span class="front-brand">Parlour 71</span>
    <span class="contact-name">Mira Dunwoody</span>
    <span class="contact-phone">043 127 9406</span>
    <span class="contact-address">71 Orchard Crescent, Tallow Bend</span>
  </section>

</body>
</html>
```